Leading In-Home Tutoring Company Needs Web Banners

We need a suite of web banners for our re-marketing campaign. We are based in Melbourne and heading into the busiest time of the year with back to school and we would like to help guide parents to working with us via quality designed banners with the right CTAs. Banner specs as follows (W x H in pixels)
Medium Rectangle: 300 x 250
Vertical rectangle: 240 x 400
Banner: 468 x 60
Leaderboard: 728 x 90
Square: 250 x 250
Mobile leaderboard: 320 x 50
Updates

Hi designers I'm new to this and didn't realise that I had to upload all files at the beginning. I have images that can be used for this project. Just need to work out how to upload them. Added Sunday, January 22, 2017

Hi awesome designers... I've updated the brief now with new files :)

Target Market(s)

Mothers who value kids education. Our customer can be found having morning coffee with friends in her lycra as she prepares to go to the gym. Middle class, inner city and suburban Mums. Most likely on Friendnook.

Industry/Entity Type

It Company

Font styles to use
Sans Serif

Colors
0692cd
fbed22
f47f39
ec1f27

Requirements
Must have
• Wording should include.
• What we do: 1:1, In-Home Tutoring
• Value proposition: The Best Tutor For Your Child
• Call to Action - Free Assessment > Find Out More
• Adjusted layout to suit the sizes. Use of image where possible to provide immediate graphic display of what we do
Nice to have
• Keep it simple, create an emotive connection. Kids matter to parents and they will pay for services if we can create banners that show we care and can help wtih their education.
Should not have
• Anything negative or use fear marketing

```html
<!DOCTYPE html>
<html lang="en">
<head>
<meta charset="utf-8">
<title>LearnWell – In-Home Tutoring Leaderboard</title>
<link rel="stylesheet" href="https://fonts.googleapis.com/css2?family=Arimo:wght@400;700&display=swap">
<style>
  :root {
    --blue-deep: #0a4fa3;
    --blue-main: #0692cd;
    --blue-light: #2fa6e0;
    --white: #ffffff;
    --cream: #fff7cf;
    --orange: #f47f39;
    --orange-dark: #e5651f;
    --photo-a: #c9b59a;
    --photo-b: #6f8fb0;
  }
  * { margin: 0; padding: 0; box-sizing: border-box; }
  html, body { width: 1200px; height: 148px; overflow: hidden; }
  body { font-family: "Arimo", Arial, sans-serif; }

  .banner {
    position: relative;
    width: 1200px;
    height: 148px;
    overflow: hidden;
    background: linear-gradient(180deg, var(--blue-light) 0%, var(--blue-main) 45%, var(--blue-deep) 100%);
    color: var(--white);
  }

  .what-we-do {
    position: absolute;
    left: 0; top: 14px;
    width: 248px;
    text-align: center;
    font-size: 25px;
    line-height: 40px;
    font-weight: 400;
  }

  .photo-bubble {
    position: absolute;
    left: 246px; top: -4px;
    width: 296px; height: 150px;
  }

  .value {
    position: absolute;
    left: 548px; top: 14px;
    width: 240px;
    text-align: center;
  }
  .value__label { font-size: 24px; font-weight: 700; line-height: 34px; }
  .value__line { font-size: 26px; line-height: 36px; color: var(--cream); }

  .brand {
    position: absolute;
    left: 770px; top: 84px;
    display: flex; align-items: center; gap: 8px;
    font-size: 30px; font-weight: 700;
    color: var(--white);
  }
  .brand__dot {
    width: 14px; height: 14px; border-radius: 50%;
    background: var(--orange);
  }

  .cta {
    position: absolute;
    left: 969px; top: 0;
    width: 231px; height: 148px;
    background: linear-gradient(180deg, var(--orange) 0%, var(--orange-dark) 100%);
    display: flex; flex-direction: column; justify-content: center; align-items: center;
    text-align: center;
    font-size: 22px; line-height: 30px; font-weight: 400;
    text-transform: uppercase;
  }
</style>
</head>
<body>
  <div class="banner">
    <div class="what-we-do">
      <div>What we do1:1</div>
      <div>In-Home</div>
      <div>Tutoring</div>
    </div>

    <svg class="photo-bubble" viewBox="0 0 296 150" role="img" aria-label="Photo of a tutor helping a smiling schoolgirl with her work at home">
      <defs>
        <linearGradient id="photoFill" x1="0" y1="0" x2="1" y2="1">
          <stop offset="0" stop-color="var(--photo-b)"/>
          <stop offset="0.5" stop-color="var(--photo-a)"/>
          <stop offset="1" stop-color="var(--photo-b)"/>
        </linearGradient>
      </defs>
      <path d="M12 4 H284 Q292 4 292 14 V120 Q292 132 280 132 H60 L26 148 L34 132 H16 Q6 132 6 120 V14 Q6 4 12 4 Z"
            fill="url(#photoFill)" stroke="var(--white)" stroke-width="5"/>
    </svg>

    <div class="value">
      <div class="value__label">Value proposition</div>
      <div class="value__line">The Best Tutor</div>
      <div class="value__line">ForYour Child</div>
    </div>

    <div class="brand">
      <span>LearnWell</span>
      <span class="brand__dot"></span>
    </div>

    <div class="cta">
      <div>Call to action</div>
      <div>Free</div>
      <div>Assessment &gt;</div>
      <div>Find out more</div>
    </div>
  </div>
</body>
</html>
```